Business Card Design Project

I have established a company called "Tidewell" which is a business specialising in psychotherapy/counselling , predominantly for anxiety & depression.

My name is Mel....hence, the Tidewell link. However, Tidewell was also chosen for its reference to green shoots of growth/recovery.

Tidewell is to be "upmarket" and highly professional. I'm keen for the style and colours to reflect this.....taupe/grey with navy/black script, for example.....NO primary colours.

My name needs to be on the card and my mobile number. Not sure, but suspect it should also have my qualifications ( BA (Psych) & BSc (Hons) Psychology). Mobile number 0463 918 207.

```html
<!DOCTYPE html>
<html lang="en">
<head>
<meta charset="utf-8">
<title>Tidewell – Business Card</title>
<link rel="stylesheet" href="https://fonts.googleapis.com/css2?family=Arimo:wght@700&display=swap">
<style>
  :root {
    --backdrop: #a98f6e;
    --card: #171412;
    --gold: #cdbb8c;
    --muted: #4d4640;
  }
  * { margin: 0; padding: 0; box-sizing: border-box; }
  html, body {
    width: 1200px;
    height: 798px;
    overflow: hidden;
    background: var(--backdrop);
  }
  .canvas {
    position: relative;
    width: 1200px;
    height: 798px;
  }
  .card {
    position: absolute;
    left: 365px;
    top: 44px;
    width: 470px;
    height: 710px;
    background: var(--card);
    font-family: "Arimo", Arial, sans-serif;
    font-weight: 700;
    text-transform: uppercase;
  }
  .brand {
    position: absolute;
    top: 210px;
    left: 0;
    right: 0;
    text-align: center;
    color: var(--gold);
    font-size: 58px;
    letter-spacing: 2px;
    line-height: 1;
  }
  .details {
    position: absolute;
    top: 358px;
    left: 0;
    right: 0;
    text-align: center;
    color: var(--gold);
    font-size: 17px;
    line-height: 1.3;
    letter-spacing: 0.3px;
  }
  .details .soft { color: var(--muted); }
  .footer-brand {
    position: absolute;
    right: 22px;
    bottom: 20px;
    color: var(--muted);
    font-size: 16px;
    letter-spacing: 0.5px;
  }
</style>
</head>
<body>
<main class="canvas">
  <section class="card" aria-label="Tidewell business card">
    <h1 class="brand">Tidewell</h1>
    <div class="details">
      <p class="name-line">Mel <span class="soft">Psychotherapist</span></p>
      <p class="phone-line">Phone - 0463 918 207</p>
      <p class="qualifications">BA <span class="soft">(Psych)</span> &amp; BSc <span class="soft">(Hons)</span> Psychology</p>
    </div>
    <p class="footer-brand">Tidewell</p>
  </section>
</main>
</body>
</html>
```